brivox new business card design project

we need a new business card design. you can view info about us @ brivox.com. i have attached an example of our previous card with our previous name that we no longer use. We really liked the design, colors etc. look below to see more info about this project. it asks for a limited number of words. please see our website for more info about our compnay.

Target Market(s)

law enforcement

Contact Information for Business Card

i have uploaded an example of what we used before that we liked.

Font styles to use
Serif

```html
<!DOCTYPE html>
<html lang="en">
<head>
<meta charset="utf-8">
<title>Brivox Business Card</title>
<link href="https://fonts.googleapis.com/css2?family=Lato:wght@300;700&family=Open+Sans:wght@400;600&display=swap" rel="stylesheet">
<style>
  :root {
    --backdrop: #e8e5e0;
    --card-navy: #021824;
    --pattern-deep: #071c2b;
    --pattern-mid: #123449;
    --pattern-glow: #1d4a60;
    --ink-light: #ffffff;
    --ink-soft: #e3e8ec;
    --rule: #7f8d96;
  }
  * { margin: 0; padding: 0; box-sizing: border-box; }
  html, body {
    width: 1200px;
    height: 900px;
    overflow: hidden;
    background: var(--backdrop);
  }
  .canvas {
    position: relative;
    width: 1200px;
    height: 900px;
  }
  .card {
    position: absolute;
    left: 330px;
    width: 556px;
    height: 343px;
    box-shadow: 3px 4px 8px rgba(0, 0, 0, 0.35);
    overflow: hidden;
  }
  /* Back side: contact details */
  .card--contact {
    top: 90px;
    background: var(--card-navy);
    color: var(--ink-soft);
    font-family: "Open Sans", Arial, sans-serif;
    text-align: center;
  }
  .contact-name {
    position: absolute;
    top: 63px;
    left: 0;
    right: 0;
    font-family: "Lato", Arial, sans-serif;
    font-weight: 700;
    font-size: 21px;
    color: var(--ink-light);
    letter-spacing: 0.2px;
  }
  .contact-role {
    position: absolute;
    top: 86px;
    left: 0;
    right: 0;
    font-size: 16px;
  }
  .contact-rule {
    position: absolute;
    left: 205px;
    width: 146px;
    height: 1px;
    background: var(--rule);
  }
  .contact-rule--upper { top: 117px; }
  .contact-rule--lower { top: 206px; }
  .contact-lines {
    position: absolute;
    top: 128px;
    left: 0;
    right: 0;
    list-style: none;
    font-size: 16px;
    line-height: 20px;
  }
  .contact-lines b { font-weight: 600; color: var(--ink-light); }
  .contact-address {
    position: absolute;
    top: 224px;
    left: 0;
    right: 0;
    font-style: normal;
    font-size: 16px;
    line-height: 20px;
  }
  /* Front side: brand */
  .card--brand {
    top: 470px;
    width: 558px;
    background: var(--pattern-deep);
  }
  .brand-backdrop {
    position: absolute;
    inset: 0;
    background:
      radial-gradient(ellipse 60% 45% at 55% 100%, var(--pattern-glow) 0%, transparent 70%),
      radial-gradient(ellipse 80% 60% at 50% 40%, var(--pattern-mid) 0%, transparent 75%),
      var(--pattern-deep);
  }
  .brand-name {
    position: absolute;
    top: 136px;
    left: 0;
    right: 0;
    text-align: center;
    font-family: "Lato", Arial, sans-serif;
    font-weight: 300;
    font-size: 62px;
    letter-spacing: 6px;
    color: var(--ink-light);
  }
  .brand-tagline {
    position: absolute;
    top: 282px;
    left: 0;
    right: 0;
    text-align: center;
    font-family: "Lato", Arial, sans-serif;
    font-weight: 700;
    font-size: 15.5px;
    letter-spacing: 0.3px;
    color: var(--ink-light);
  }
</style>
</head>
<body>
<main class="canvas">
  <section class="card card--contact" aria-label="Business card back">
    <h1 class="contact-name">MARCUS HALE</h1>
    <p class="contact-role">Managing Director</p>
    <div class="contact-rule contact-rule--upper"></div>
    <ul class="contact-lines">
      <li><b>P:</b> 866.555.0142</li>
      <li><b>E:</b> info@brivox.com</li>
      <li><b>W:</b> www.brivox.com</li>
    </ul>
    <div class="contact-rule contact-rule--lower"></div>
    <address class="contact-address">
      4180 Larkspur Drive<br>
      Austin, TX 78745
    </address>
  </section>

  <section class="card card--brand" aria-label="Business card front">
    <div class="brand-backdrop" role="img" aria-label="Dark blue network pattern of connected dots and lines"></div>
    <p class="brand-name">BRIVOX</p>
    <p class="brand-tagline">LAW ENFORCEMENT INNOVATION</p>
  </section>
</main>
</body>
</html>
```